Business Card Design

Selling beds and mattrices
See website www.lunorest.com.au for details
Targeting wholesale bed sellers

Industry/Entity Type

Business

Contact Information for Business Card

Lunorest
Director Gerald Whitcombe
Beds and Mattrices - Most technologically advanced beds in the world
European designed and made
Already No 1 seller in Europe
Call now for a quote
ph: 0472 518 306
Email: sales@lunorest.com.au
www.lunorest.com.au

```html
<!DOCTYPE html>
<html lang="en">
<head>
<meta charset="utf-8">
<title>Lunorest Business Card</title>
<link href="https://fonts.googleapis.com/css2?family=Open+Sans:wght@400;600;700;800&display=swap" rel="stylesheet">
<style>
  :root {
    --backdrop: #2a1214;
    --card: #ececec;
    --card-low: #e4e3e3;
    --photo-light: #f4f4f4;
    --photo-mid: #c9c9c9;
    --photo-dark: #9e9e9e;
    --ink: #111111;
    --ink-soft: #333333;
    --grey: #7d7d7d;
    --band: #0a0a0a;
    --band-text: #ffffff;
  }
  * { box-sizing: border-box; margin: 0; padding: 0; }
  html, body {
    width: 1200px; height: 800px; overflow: hidden;
    background: var(--backdrop);
    font-family: "Open Sans", Arial, sans-serif;
  }
  .card {
    position: absolute; left: 75px; top: 100px;
    width: 1050px; height: 600px;
    background: linear-gradient(180deg, var(--card) 0%, var(--card-low) 100%);
    overflow: hidden;
  }
  .card__photo {
    position: absolute; left: 0; top: 0; width: 100%; height: 330px;
    background:
      linear-gradient(90deg, rgba(150,150,150,.55) 0%, rgba(200,200,200,.2) 35%, rgba(240,240,240,.4) 70%, rgba(190,190,190,.4) 100%),
      linear-gradient(180deg, var(--photo-light) 0%, var(--photo-mid) 60%, var(--photo-dark) 100%);
    opacity: .8;
  }
  .brand {
    position: absolute; left: 150px; top: 150px;
    display: flex; align-items: center; gap: 18px;
  }
  .brand__square {
    width: 34px; height: 34px; background: var(--ink);
  }
  .brand__name {
    font-size: 76px; font-weight: 400; color: var(--ink);
    letter-spacing: .06em; text-transform: uppercase; line-height: 1;
  }
  .band {
    position: absolute; left: 0; top: 330px; width: 100%; height: 40px;
    background: var(--band);
    display: flex; align-items: center; justify-content: flex-end;
    padding-right: 60px;
  }
  .band__text {
    color: var(--band-text); font-size: 25px; font-weight: 400;
    letter-spacing: .55em;
  }
  .tagline {
    position: absolute; font-weight: 800; text-transform: uppercase;
    letter-spacing: .12em; white-space: nowrap;
  }
  .tagline--main { left: 230px; top: 380px; font-size: 21px; color: var(--ink); }
  .tagline--sub { left: 150px; top: 410px; font-size: 19px; color: var(--grey); }
  .person { position: absolute; left: 250px; top: 470px; text-align: right; }
  .person__name { font-size: 34px; font-weight: 600; color: var(--grey); line-height: 1.1; }
  .person__role { font-size: 22px; font-weight: 400; color: var(--ink-soft); }
  .divider {
    position: absolute; left: 620px; top: 455px; width: 2px; height: 110px;
    background: var(--ink-soft);
  }
  .contacts {
    position: absolute; left: 645px; top: 458px; list-style: none;
  }
  .contacts li {
    display: flex; align-items: center; gap: 10px;
    font-size: 23px; color: var(--ink); line-height: 34px;
  }
  .contacts svg { width: 22px; height: 22px; fill: var(--ink-soft); flex: none; }
</style>
</head>
<body>
  <div class="card">
    <div class="card__photo" role="img" aria-label="Faded black and white photograph of a modern bedroom with a bed and side furniture"></div>

    <div class="brand">
      <span class="brand__square"></span>
      <span class="brand__name">Lunorest</span>
    </div>

    <div class="band"><span class="band__text">Beds and Mattrices</span></div>

    <p class="tagline tagline--main">Most technologically advanced beds in the world</p>
    <p class="tagline tagline--sub">European designed and made already No 1 seller in Europe</p>

    <div class="person">
      <p class="person__name">Gerald Whitcombe</p>
      <p class="person__role">Director</p>
    </div>

    <div class="divider"></div>

    <ul class="contacts">
      <li>
        <svg viewBox="0 0 24 24" aria-hidden="true"><path d="M6.6 10.8a15.1 15.1 0 0 0 6.6 6.6l2.2-2.2a1 1 0 0 1 1-.25 11.4 11.4 0 0 0 3.6.57 1 1 0 0 1 1 1V20a1 1 0 0 1-1 1A17 17 0 0 1 3 4a1 1 0 0 1 1-1h3.5a1 1 0 0 1 1 1c0 1.25.2 2.45.57 3.6a1 1 0 0 1-.25 1z"/></svg>
        0472 518 306
      </li>
      <li>
        <svg viewBox="0 0 24 24" aria-hidden="true"><path d="M3 5h18a1 1 0 0 1 1 1v12a1 1 0 0 1-1 1H3a1 1 0 0 1-1-1V6a1 1 0 0 1 1-1zm1 2.3V17h16V7.3l-8 5.2z M4.5 7h15L12 11.8z"/></svg>
        sales@lunorest.com.au
      </li>
      <li>
        <svg viewBox="0 0 24 24" aria-hidden="true"><path d="M12 2a10 10 0 1 0 0 20 10 10 0 0 0 0-20zm6.9 6h-2.9a15.6 15.6 0 0 0-1.4-3.6A8 8 0 0 1 18.9 8zM12 4a14 14 0 0 1 1.9 4h-3.8A14 14 0 0 1 12 4zM4.3 14a8.2 8.2 0 0 1 0-4h3.4a16.5 16.5 0 0 0 0 4zm.8 2h2.9a15.6 15.6 0 0 0 1.4 3.6A8 8 0 0 1 5.1 16zM8 8H5.1a8 8 0 0 1 4.3-3.6A15.6 15.6 0 0 0 8 8zm4 12a14 14 0 0 1-1.9-4h3.8A14 14 0 0 1 12 20zm2.3-6H9.7a14.7 14.7 0 0 1 0-4h4.6a14.7 14.7 0 0 1 0 4zm.3 5.6a15.6 15.6 0 0 0 1.4-3.6h2.9a8 8 0 0 1-4.3 3.6zm1.7-5.6a16.5 16.5 0 0 0 0-4h3.4a8.2 8.2 0 0 1 0 4z"/></svg>
        www.lunorest.com.au
      </li>
    </ul>
  </div>
</body>
</html>
```